Business Card for Marco Thieblin Analytics and Marco Thieblin Photography

I want a double sided business card: on one side it should be about "Marco Thieblin Photography" and on the other side about "Marco Thieblin Analytics". You find the logos for these two projects in the attachments. The design of the business card should blend well with the colours and fonts used in the logos and should be quite simple, yet look professional and modern.

In addition to my name, there should be content for a telephone number, e-mail address and website. There should be little icons (for telephone, email and web) before these fields. I do not want a postal mail address field.
Lastly you should indicate that people can contact me in the following languages: Lëtzebuergesch, Deutsch, Français, English, Castellano, Ido
This should be very unobtrusive: either in a small muted font or with little icons (preferably without using flags as flags represent nations, not languages - one possibility would be by using the 2 letter ISO codes).

The design should be delivered in Adobe Illustrator format or something similar that I can edit easily, as it's possible that I will change my e-mail address and domain soon.

I hope this was detailed enough but still leaves you some freedom for designing something nice.

Thank you!
Marco

Industry/Entity Type

Business

Contact Information for Business Card

e-mail address: mtb_@orvenmail.example
website: www.marcothieblin.example (for Marco Thieblin Photography)
website: kelvodata.example/mtb (for Marco Thieblin Analytics - this address is likely to change)
phone: +352 691 987 654 (not my real number - I prefer not to publish it on the web)

Requirements
Nice to have
• A speech bubble followed by the 2-letter language codes (lb, de, fr, en, es, io) or even speech bubble icons for every language would be nice and eliminates the need to put text like 'you can contact me in the following languages'.

```html
<!DOCTYPE html>
<html lang="en">
<head>
<meta charset="utf-8">
<title>Marco Thieblin – Business Cards</title>
<link href="https://fonts.googleapis.com/css2?family=Open+Sans:wght@400;600;700&family=Italianno&display=swap" rel="stylesheet">
<style>
  :root {
    --backdrop: #35302d;
    --card-white: #ffffff;
    --card-grey: #e5e5e5;
    --brand-orange: #f0882a;
    --brand-green: #3bb54a;
    --ink: #3a3a3a;
    --on-green: #ffffff;
  }
  * { box-sizing: border-box; margin: 0; padding: 0; }
  html, body {
    width: 1200px; height: 844px; overflow: hidden;
    background: var(--backdrop);
    font-family: "Open Sans", Arial, sans-serif;
  }
  .stage { position: relative; width: 1200px; height: 844px; }

  .card {
    position: absolute;
    width: 520px; height: 300px;
    border-radius: 3px;
    overflow: hidden;
  }

  /* Photography side */
  .card--photography { left: 60px; top: 420px; background: var(--card-white); }
  .owner-name {
    position: absolute; left: 34px; top: 44px;
    font-size: 20px; font-weight: 700; letter-spacing: 0.2px;
    color: var(--brand-orange); text-transform: uppercase;
  }
  .brand-name {
    position: absolute;
    display: flex; align-items: center; gap: 10px;
    font-weight: 600; color: var(--brand-orange);
  }
  .brand-name__dot {
    width: 18px; height: 18px; border-radius: 50%;
    background: var(--brand-orange); flex: none;
  }
  .card--photography .brand-name { left: 250px; top: 96px; width: 240px; font-size: 20px; line-height: 1.2; }

  .contact-list {
    position: absolute; left: 34px; bottom: 30px;
    list-style: none; display: grid; gap: 4px;
  }
  .contact-list__item {
    display: flex; align-items: center; gap: 10px;
    font-size: 15px; color: var(--ink);
  }
  .contact-list__icon { width: 13px; height: 13px; flex: none; }

  /* Analytics side */
  .card--analytics { left: 620px; top: 90px; background: var(--card-grey); }
  .card--analytics .brand-name {
    left: 0; right: 0; top: 70px; justify-content: center;
    font-size: 24px;
  }
  .language-band {
    position: absolute; left: 0; right: 0; top: 178px; height: 92px;
    background: var(--brand-green); color: var(--on-green);
    text-align: center; padding-top: 12px;
  }
  .language-band__lead {
    font-family: "Italianno", cursive;
    font-size: 30px; line-height: 1;
  }
  .language-band__list {
    list-style: none; margin-top: 10px;
    display: flex; justify-content: center; gap: 0;
    font-size: 12.5px; font-weight: 600;
  }
  .language-band__list li + li::before { content: "|"; margin: 0 6px; font-weight: 400; }
</style>
</head>
<body>
<main class="stage">

  <section class="card card--photography" aria-label="Photography side">
    <h1 class="owner-name">Marco Thieblin</h1>
    <div class="brand-name"><span class="brand-name__dot"></span><span>Marco Thieblin Photography</span></div>
    <ul class="contact-list">
      <li class="contact-list__item">
        <svg class="contact-list__icon" viewBox="0 0 16 16" aria-hidden="true"><path fill="#f0882a" d="M3.5 1.5l2.5 3-1.6 1.6c.9 2 2.5 3.6 4.5 4.5L10.5 9l3 2.5-1.5 2.5C6.5 14 2 9.5 1.9 3z"/></svg>
        <span>+352 691 987 654</span>
      </li>
      <li class="contact-list__item">
        <svg class="contact-list__icon" viewBox="0 0 16 16" aria-hidden="true"><rect x="1" y="3" width="14" height="10" rx="1" fill="#f0882a"/><path d="M1.5 3.5L8 9l6.5-5.5" stroke="#fff" stroke-width="1.3" fill="none"/></svg>
        <span>mtb_@orvenmail.example</span>
      </li>
      <li class="contact-list__item">
        <svg class="contact-list__icon" viewBox="0 0 16 16" aria-hidden="true"><circle cx="8" cy="8" r="7" fill="#f0882a"/><path d="M1 8h14M8 1c-3 3.5-3 10.5 0 14M8 1c3 3.5 3 10.5 0 14" stroke="#fff" stroke-width="1.1" fill="none"/></svg>
        <span>www.marcothieblin.example</span>
      </li>
    </ul>
  </section>

  <section class="card card--analytics" aria-label="Analytics side">
    <div class="brand-name"><span class="brand-name__dot"></span><span>Marco Thieblin Analytics</span></div>
    <div class="language-band">
      <p class="language-band__lead">We speak you in the following languages:</p>
      <ul class="language-band__list">
        <li>Lëtzebuergesch</li><li>Deutsch</li><li>Français</li><li>English</li><li>Castellano</li><li>Ido</li>
      </ul>
    </div>
  </section>

</main>
</body>
</html>
```